Designing a billboard

Should have
Corwell & Pine, LLC
Ph: 512-647-3918
Auto Accidents / Personal Injury
Family Law
Criminal Defense
Real Estate
Free Consultation

Target Market(s)

Legal

Industry/Entity Type

Legal

Font styles to use
Serif
Sans Serif

Requirements
Must have
• Designing a billboard

Should have
Corwell & Pine, LLC
Ph: 512-647-3918
Family Law
Criminal Defense
Real Estate
Free Consultation
Nice to have
• Nice to have info above
Should not have
• None

```html
<!DOCTYPE html>
<html lang="en">
<head>
<meta charset="UTF-8">
<title>Corwell &amp; Pine, LLC Billboard</title>
<link rel="stylesheet" href="https://fonts.googleapis.com/css2?family=Tinos:ital,wght@0,700;1,700&display=swap">
<style>
  :root {
    --page-bg: #e6e8ee;
    --board-tan: #b8ae86;
    --ink-dark: #232323;
    --title-white: #f7f5f0;
    --photo-warm: #8c4a4a;
    --photo-mid: #5c5150;
    --photo-cool: #3c3d42;
  }
  html, body {
    margin: 0;
    padding: 0;
    width: 1200px;
    height: 800px;
    overflow: hidden;
    background: var(--page-bg);
  }
  .billboard {
    position: absolute;
    left: 40px;
    top: 100px;
    width: 1120px;
    height: 600px;
    background: var(--board-tan);
    overflow: hidden;
    font-family: "Tinos", "Times New Roman", serif;
  }
  .hero-photo {
    position: absolute;
    inset: 0;
    width: 1120px;
    height: 600px;
  }
  .firm-name {
    position: absolute;
    left: 345px;
    top: 28px;
    width: 760px;
    margin: 0;
    text-align: right;
    font-size: 66px;
    font-weight: 700;
    color: var(--title-white);
    text-shadow: 3px 4px 5px rgba(0,0,0,0.55);
    white-space: nowrap;
  }
  .practice-areas {
    position: absolute;
    left: 34px;
    top: 112px;
    margin: 0;
    padding: 0;
    list-style: none;
    font-size: 33px;
    font-weight: 700;
    line-height: 40px;
    color: var(--ink-dark);
  }
  .phone-number {
    position: absolute;
    left: 120px;
    top: 438px;
    margin: 0;
    font-size: 150px;
    font-weight: 700;
    line-height: 1;
    letter-spacing: 1px;
    color: var(--ink-dark);
    white-space: nowrap;
  }
</style>
</head>
<body>
  <div class="billboard">
    <svg class="hero-photo" viewBox="0 0 1120 600" role="img" aria-label="Photo of a bronze Lady Justice statue holding scales beside law books, in warm red and dark grey tones">
      <defs>
        <linearGradient id="photoTone" x1="0" y1="0" x2="1" y2="0.4">
          <stop offset="0" stop-color="var(--photo-warm)"/>
          <stop offset="0.45" stop-color="var(--photo-mid)"/>
          <stop offset="1" stop-color="var(--photo-cool)"/>
        </linearGradient>
      </defs>
      <polygon points="325,0 1120,0 1120,468 437,468" fill="url(#photoTone)"/>
    </svg>

    <h1 class="firm-name">Corwell &amp; Pine, LLC</h1>

    <ul class="practice-areas">
      <li>Auto Accidents</li>
      <li>Personal Injury</li>
      <li>Family Law</li>
      <li>Criminal Defense</li>
      <li>Real Estate</li>
      <li>Free Consultation</li>
    </ul>

    <p class="phone-number">512-647-3918</p>
  </div>
</body>
</html>
```